Unternehmen für Ordnung und Sauberkeit am Arbeitsplatz und Produkte zur Produktionsoptimierung benötigt Visitenkarten und Briefpapier
Zielgruppe
Produkte für Ordnung und Sauberkeit am Arbeitsplatz, Organisation von Arbeitsplätzen, Produkte zur Vereinfachung von Arbeitsabläufen, Produkte zur Produktionsoptimierung unter dem Lean Gedanke, Schlagwort: "5S", nachhaltig, sauber
Aufgabenstellung
Wir sind auf der Suche nach Visitenkarten und Briefpapier für das Unternehmen ourKarto. Nachhaltig, Sauber usw.. Unser Firmenlogo finden Sie anbei.

```html
<!DOCTYPE html>
<html lang="de">
<head>
<meta charset="utf-8">
<title>ourKarto – Briefpapier und Visitenkarte</title>
<link rel="stylesheet" href="https://fonts.googleapis.com/css2?family=Hind:wght@400;500;600&display=swap">
<style>
  :root {
    --backdrop: #ececec;
    --paper: #fbfbfb;
    --card: #ffffff;
    --ink: #1c1c1c;
    --muted: #8d8d8d;
    --rule: #dedede;
    --name-ink: #3a3a3a;
  }
  html, body {
    margin: 0;
    padding: 0;
    width: 1200px;
    height: 900px;
    overflow: hidden;
    background: var(--backdrop);
    font-family: "Hind", Arial, sans-serif;
  }
  .canvas { position: relative; width: 1200px; height: 900px; }

  /* Letterhead */
  .letterhead {
    position: absolute;
    left: 146px; top: 56px;
    width: 562px; height: 789px;
    background: var(--paper);
    box-shadow: 2px 3px 5px rgba(0,0,0,.35);
  }
  .rules { position: absolute; display: flex; gap: 5px; }
  .rules span { width: 3px; background: var(--rule); height: 100%; }
  .letterhead .rules { left: 76px; top: 0; height: 660px; }

  .company-name {
    position: absolute;
    margin: 0;
    color: var(--name-ink);
    font-weight: 500;
    line-height: 1;
    background: var(--paper);
  }
  .letterhead .company-name { left: 32px; top: 34px; font-size: 44px; padding-right: 6px; }

  .letter-body {
    position: absolute;
    left: 147px; top: 190px;
    color: var(--ink);
    font-size: 12px;
    letter-spacing: 0.15px;
    line-height: 14.4px;
    white-space: nowrap;
  }
  .letter-subject { margin: 0 0 40px; font-size: 12.5px; line-height: 16px; font-weight: 500; letter-spacing: 0; }
  .letter-body p { margin: 0 0 14.4px; }

  .letter-footer { position: absolute; left: 80px; top: 669px; }
  .contact-row { display: flex; align-items: flex-start; gap: 11px; margin-bottom: 9px; }
  .contact-row svg { width: 12px; height: 12px; fill: #c9c9c9; flex: none; }
  .contact-row div { color: var(--muted); font-size: 7.5px; line-height: 10px; }

  .signature-block { position: absolute; left: 380px; top: 658px; width: 120px; }
  .signature-role { font-size: 10.5px; color: var(--ink); margin: 0 0 0 19px; }
  .signature-mark {
    width: 118px; height: 22px; margin-top: 2px;
    background: linear-gradient(90deg, rgba(58,127,224,.15), rgba(58,127,224,.35), rgba(58,127,224,.15));
    border-radius: 3px;
  }

  /* Business card */
  .business-card {
    position: absolute;
    left: 682px; top: 218px;
    width: 229px; height: 400px;
    background: var(--card);
    box-shadow: 2px 3px 5px rgba(0,0,0,.35);
  }
  .business-card .rules { left: 106px; top: 0; height: 214px; gap: 4px; }
  .business-card .rules span { width: 2px; }
  .business-card .company-name { left: 58px; top: 30px; font-size: 27px; padding-right: 4px; background: var(--card); }

  .card-icon { position: absolute; top: 219px; width: 10px; height: 10px; fill: #c9c9c9; }
  .card-line {
    position: absolute; top: 244px;
    writing-mode: vertical-rl;
    color: var(--muted);
    font-size: 7px; line-height: 8px;
    white-space: nowrap;
  }
</style>
</head>
<body>
<main class="canvas">

  <section class="letterhead" aria-label="Briefpapier">
    <div class="rules" aria-hidden="true"><span></span><span></span><span></span></div>
    <p class="company-name">ourKarto</p>

    <article class="letter-body">
      <h1 class="letter-subject">Dolorem Ipsum</h1>
      <p>Sed ut perspiciatis unde omnis iste natus error sit voluptatem<br>
accusantium doloremque laudantium, totam rem aperiam, eaque<br>
ipsa quae ab illo inventore veritatis et quasi architecto beatae<br>
vitae dicta sunt explicabo. Nemo enim ipsam voluptatem quia<br>
voluptas sit aspernatur aut odit aut fugit, sed quia consequuntur<br>
magni dolores eos qui ratione voluptatem sequi nesciunt. Neque<br>
porro quisquam est, qui dolorem ipsum quia dolor sit amet,<br>
consectetur, adipisci velit, sed quia non numquam eius modi<br>
tempora incidunt ut labore et dolore magnam aliquam quaerat<br>
voluptatem. Ut enim ad minima veniam, quis nostrum<br>
exercitationem ullam corporis suscipit laboriosam, nisi ut aliquid<br>
ex ea commodi consequatur? Quis autem vel eum iure<br>
reprehenderit qui in ea voluptate velit esse quam nihil molestiae<br>
consequatur, vel illum qui dolorem eum fugiat quo voluptas nulla<br>
pariatur</p>
      <p>Neque porro quisquam est, qui dolorem ipsum quia dolor sit amet,<br>
consectetur, adipisci velit, sed quia non numquam eius modi<br>
tempora incidunt ut labore et dolore magnam aliquam quaerat<br>
voluptatem. Ut enim ad minima veniam, quis nostrum<br>
exercitationem ullam corporis suscipit laboriosam, nisi ut aliquid<br>
ex ea commodi consequatur? Quis autem vel eum iure<br>
reprehenderit qui in ea voluptate velit esse quam nihil molestiae<br>
consequatur, vel illum qui dolorem eum fugiat quo voluptas nulla<br>
pariatur.</p>
    </article>

    <footer class="letter-footer">
      <div class="contact-row">
        <svg viewBox="0 0 12 12" aria-hidden="true"><circle cx="6" cy="3.5" r="2.7"/><path d="M1 12c0-3.5 2.2-5 5-5s5 1.5 5 5z"/></svg>
        <div>Geschäftsführer: Name Nachname</div>
      </div>
      <div class="contact-row">
        <svg viewBox="0 0 12 12" aria-hidden="true"><path d="M2.5 1l2 2.5-1.2 1.3c.7 1.6 2 2.9 3.6 3.6L8.2 7.2 11 9.2 9.6 11C5 10.6 1.4 7 1 2.4z"/></svg>
        <div>Tel.: +49 (0) 123 456 789<br>Fax: +49 (0) 123 456 789</div>
      </div>
      <div class="contact-row">
        <svg viewBox="0 0 12 12" aria-hidden="true"><path d="M5 0l7 5-3 1-1 3-2-2-4 5 3-5-2-2 3-1z"/></svg>
        <div>Musterstrasse 10<br>D - 12345 Musterstadt</div>
      </div>
      <div class="contact-row">
        <svg viewBox="0 0 12 12" aria-hidden="true"><path d="M0 2h12v8H0zm1 1v.4l5 3.3 5-3.3V3zm0 1.6V9h10V4.6L6 8z"/></svg>
        <div>Info@ourkarto.de<br>www.our-karto.de</div>
      </div>
    </footer>

    <div class="signature-block">
      <p class="signature-role">Geschäftsführer</p>
      <div class="signature-mark" role="img" aria-label="Handschriftliche Unterschrift Name Nachname"></div>
    </div>
  </section>

  <section class="business-card" aria-label="Visitenkarte">
    <div class="rules" aria-hidden="true"><span></span><span></span><span></span></div>
    <p class="company-name">ourKarto</p>

    <svg class="card-icon" style="left:72px" viewBox="0 0 12 12" aria-hidden="true"><path d="M2 0h8v12H2zm1 1v10h6V1z"/></svg>
    <svg class="card-icon" style="left:98px" viewBox="0 0 12 12" aria-hidden="true"><path d="M5 0l7 5-3 1-1 3-2-2-4 5 3-5-2-2 3-1z"/></svg>
    <svg class="card-icon" style="left:126px" viewBox="0 0 12 12" aria-hidden="true"><path d="M2.5 1l2 2.5-1.2 1.3c.7 1.6 2 2.9 3.6 3.6L8.2 7.2 11 9.2 9.6 11C5 10.6 1.4 7 1 2.4z"/></svg>
    <svg class="card-icon" style="left:151px" viewBox="0 0 12 12" aria-hidden="true"><circle cx="6" cy="3.5" r="2.7"/><path d="M1 12c0-3.5 2.2-5 5-5s5 1.5 5 5z"/></svg>

    <div class="card-line" style="left:152px">Geschäftsführer: Name Nachname</div>
    <div class="card-line" style="left:134px">Tel.: +49 (0) 123 456 789</div>
    <div class="card-line" style="left:125px">Fax: +49 (0) 123 456 789</div>
    <div class="card-line" style="left:105px">Musterstrasse 10</div>
    <div class="card-line" style="left:96px">D - 12345 Musterstadt</div>
    <div class="card-line" style="left:78px">Info@ourkarto.de</div>
    <div class="card-line" style="left:69px">www.our-karto.de</div>
  </section>

</main>
</body>
</html>
```